Rack card 4"x9" for a construction company

We need to have a design for:
- the holder of rack cards. Letter size
- and the rack cards. Size 4"x9"

I attached a picture of the sample holder for example.

I am putting some of the brochures and pics we have in:

https://files.quillbarrow.net/folders/7Tz4Qm9WpXc2Lr8VbN3kHs6JdYf0aGeUo?usp=sharing

The Bodoni font is on the drive.
The rack card should call to action - to learn about our projects and that we are offering fixed price packages.

One of the sides of the rack card has to show our houses like we show on the website ferncove-builders.ca
Images with short info like on the website http://www.ferncove-builders.ca/our-projects/
Maybe have something like: Learn more about our recent projects at www...

You can use our logo from th pdf files. In the brochure on the cover page we show all the associations we are member of - this is a must to be shown.

Mentioning the website and the phone number is a must.

Bring your ideas.
Don't hesitate to ask questions.

Thanks
Harold

```html
<!DOCTYPE html>
<html lang="en">
<head>
<meta charset="utf-8">
<title>Ferncove Builders – Rack Card</title>
<link rel="stylesheet" href="https://fonts.googleapis.com/css2?family=Bodoni+Moda:wght@400;500;700&family=Open+Sans:wght@300;400&family=Oswald:wght@500&display=swap">
<style>
  :root {
    --navy: #0f2240;
    --gold: #bfb092;
    --panel: #ecedec;
    --paper: #ffffff;
    --ground: #e6e4e0;
    --ink: #4a4a4a;
    --sky: #9cc7e6;
    --lawn: #5d7a3e;
  }
  * { box-sizing: border-box; margin: 0; padding: 0; }
  html, body { width: 1165px; height: 1200px; overflow: hidden; }
  body { background: var(--ground); position: relative; font-family: "Bodoni Moda", serif; }

  .card { position: absolute; left: 84px; width: 997px; height: 442px; background: var(--paper); overflow: hidden; box-shadow: 0 6px 14px rgba(0,0,0,.18); }
  .card--front { top: 60px; }
  .card--back { top: 648px; }

  /* front */
  .corner-wedge { position: absolute; left: 0; top: 0; width: 262px; height: 363px; }
  .hero-photo { position: absolute; left: 32px; top: 35px; width: 938px; height: 310px;
    background: linear-gradient(180deg, var(--sky) 0%, #b9d3e6 45%, #6b6f70 62%, #4f5b44 88%, var(--lawn) 100%); }
  .headline { position: absolute; left: 54px; top: 52px; color: #fff; font-weight: 700; font-size: 43px; line-height: 42px; text-shadow: 0 1px 3px rgba(0,0,0,.35); }
  .offer-box { position: absolute; left: 631px; top: 0; width: 233px; height: 239px; background: var(--gold); color: #fff; text-align: center; font-weight: 700; font-size: 21px; line-height: 27px; padding-top: 52px; }
  .offer-box .rule { width: 46px; height: 2px; background: #fff; margin: 13px auto 15px; }
  .thumb-strip { position: absolute; left: 538px; top: 239px; width: 393px; height: 106px; background: var(--paper); }
  .thumb { position: absolute; top: 17px; width: 109px; height: 87px; }
  .thumb--1 { left: 16px; background: linear-gradient(180deg, #8fb5d8 0%, #d9cfc0 50%, #7b8a5c 100%); }
  .thumb--2 { left: 140px; background: linear-gradient(180deg, #9cc0e0 0%, #5c7ea8 55%, #4a5a3c 100%); }
  .thumb--3 { left: 267px; background: linear-gradient(180deg, #b3cfe6 0%, #343a44 50%, #d8d8d4 75%, #4f6a3a 100%); }

  .brand { position: absolute; display: flex; align-items: center; gap: 10px; }
  .brand__mark { width: 14px; height: 14px; background: var(--gold); }
  .brand__name { font-weight: 700; letter-spacing: 1px; }
  .brand--front { left: 52px; top: 392px; }
  .brand--front .brand__name { color: var(--navy); font-size: 22px; }

  .cta { position: absolute; left: 350px; top: 380px; width: 245px; text-align: center; }
  .cta__lead { font-family: "Open Sans", sans-serif; font-weight: 400; font-size: 12px; color: var(--ink); }
  .cta__url { font-weight: 700; font-size: 17px; color: var(--navy); margin-top: 1px; }
  .phone-box { position: absolute; left: 631px; top: 372px; width: 233px; height: 70px; background: var(--gold); color: #fff; font-family: "Oswald", sans-serif; font-weight: 500; font-size: 29px; letter-spacing: 2px; display: flex; align-items: center; justify-content: center; }
  .social { position: absolute; left: 902px; top: 396px; display: flex; gap: 16px; }
  .social__dot { width: 20px; height: 20px; background: var(--navy); }
  .social__dot--round { border-radius: 50%; }

  /* back */
  .project { position: absolute; top: 11px; width: 318px; height: 391px; background: var(--panel); }
  .project--ashgrove { left: 12px; }
  .project--millbrook { left: 339px; }
  .project--westhaven { left: 667px; }
  .project__photo { height: 168px; }
  .project--ashgrove .project__photo { background: linear-gradient(180deg, #a7cde8 0%, #7d7f74 45%, #565a4e 75%, var(--lawn) 100%); }
  .project--millbrook .project__photo { background: linear-gradient(180deg, #bcd6ec 0%, #e9edf0 35%, #3b4350 60%, #a9aeb2 85%, #56703f 100%); }
  .project--westhaven .project__photo { background: linear-gradient(180deg, #a9c2d8 0%, #e6dccb 40%, #c9b9a2 75%, #6c7b55 100%); }
  .project__title { position: relative; height: 40px; background: var(--navy); color: #fff; font-weight: 700; font-size: 17px; display: flex; align-items: center; justify-content: center; }
  .project__title::after { content: ""; position: absolute; left: 50%; bottom: -14px; margin-left: -16px; border-left: 16px solid transparent; border-right: 16px solid transparent; border-top: 14px solid var(--navy); }
  .specs { list-style: none; text-align: center; color: #555; font-size: 16px; line-height: 23px; margin-top: 33px; }
  .specs__total { color: var(--navy); font-weight: 700; }

  .footer-band { position: absolute; left: 0; top: 402px; width: 997px; height: 41px; background: var(--gold); }
  .brand--footer { left: 24px; top: 12px; }
  .brand--footer .brand__mark { background: #fff; }
  .brand--footer .brand__name { color: #fff; font-size: 15px; }
  .footer-cta { position: absolute; right: 20px; top: 9px; color: #fff; display: flex; align-items: baseline; gap: 10px; }
  .footer-cta .cta__lead { color: #fff; font-weight: 300; }
  .footer-cta .cta__url { color: #fff; }
</style>
</head>
<body>

<section class="card card--front">
  <svg class="corner-wedge" viewBox="0 0 262 363" aria-hidden="true"><polygon points="0,0 262,0 0,363" fill="var(--navy)"/></svg>
  <div class="hero-photo" role="img" aria-label="Photo of a two-storey craftsman house with stone pillars, garden and blue sky"></div>
  <h1 class="headline">Build the<br>home of<br>your dreams.</h1>
  <div class="offer-box">
    <p>High Quailty<br>Custom Houses at<br>Affordable Prices.</p>
    <div class="rule"></div>
    <p>Fixed Price<br>Packages Available.</p>
  </div>
  <div class="thumb-strip">
    <div class="thumb thumb--1" role="img" aria-label="Photo of a cream modern home"></div>
    <div class="thumb thumb--2" role="img" aria-label="Photo of a blue traditional home"></div>
    <div class="thumb thumb--3" role="img" aria-label="Photo of a dark grey craftsman home"></div>
  </div>
  <div class="brand brand--front"><span class="brand__mark"></span><span class="brand__name">FERNCOVE BUILDERS</span></div>
  <div class="cta">
    <p class="cta__lead">Learn more about our recent projects at</p>
    <p class="cta__url">www.ferncove-builders.ca</p>
  </div>
  <div class="phone-box">604.555.0182</div>
  <div class="social"><span class="social__dot social__dot--round"></span><span class="social__dot"></span></div>
</section>

<section class="card card--back">
  <article class="project project--ashgrove">
    <div class="project__photo" role="img" aria-label="Photo of a modern craftsman house with stone pillars"></div>
    <h2 class="project__title">Ashgrove Modern Craftsman</h2>
    <ul class="specs">
      <li>Bedrooms 6</li><li>Bathrooms 7</li><li>Main Floor 1,690 Sqft</li>
      <li>Second Floor 1,355 Sqft</li><li>Basement 1,502 Sqft</li>
      <li class="specs__total">Total Floor 4,547 Sqft</li>
    </ul>
  </article>
  <article class="project project--millbrook">
    <div class="project__photo" role="img" aria-label="Photo of a grey traditional craftsman house"></div>
    <h2 class="project__title">Millbrook Traditional Craftsman</h2>
    <ul class="specs">
      <li>Bedrooms 5</li><li>Bathrooms 4</li><li>Main Floor 925 Sqft</li>
      <li>Second Floor 812 Sqft</li><li>Basement 968 Sqft</li>
      <li class="specs__total">Total Floor 2,705 Sqft</li>
    </ul>
  </article>
  <article class="project project--westhaven">
    <div class="project__photo" role="img" aria-label="Photo of a cream modern house at dusk"></div>
    <h2 class="project__title">Westhaven Modern Opulence</h2>
    <ul class="specs">
      <li>Bedrooms 4</li><li>Bathrooms 5</li><li>Main Floor 1,118 Sqft</li>
      <li>Second Floor 1,046 Sqft</li><li>Basement 1,137 Sqft</li>
      <li class="specs__total">Total Floor 3,301 Sqft</li>
    </ul>
  </article>
  <footer class="footer-band">
    <div class="brand brand--footer"><span class="brand__mark"></span><span class="brand__name">FERNCOVE BUILDERS</span></div>
    <div class="footer-cta">
      <span class="cta__lead">Learn more about our recent projects at</span>
      <span class="cta__url">www.ferncove-builders.ca</span>
    </div>
  </footer>
</section>

</body>
</html>
```